Halloway Crest Backers Guild business cards

Create a single-sided business card for the Halloway Crest Backers Guild based on the attached logo.
The additional data fields include Name, Title, Email, Phone, and website.
Please use the following as sample data:
Name: Dean Varrow
Title: Co-Founder / Investor
Email: deanvarrow@mailtern.net
Phone: 555-314-2706
Website: www.hcbackersguild.com

Target Market(s)

Start ups, entrepreneurs, venture capitalists

Industry/Entity Type

Investment

Contact Information for Business Card

Professional business card. Technology company.

Font styles to use
Serif
Sans Serif

Requirements
Must have
• Include the HCBG logo (attached)
• Name
• Title
• Email
• Phone
• Website
Should not have
• Cute, cartoony

```html
<!DOCTYPE html>
<html lang="en">
<head>
<meta charset="utf-8">
<title>Halloway Crest Backers Guild – Business Card</title>
<link rel="stylesheet" href="https://fonts.googleapis.com/css2?family=Roboto+Condensed:wght@400;700&display=swap">
<style>
  :root {
    --page-bg: #ecebe7;
    --card-white: #fbfcfd;
    --green-light: #2fa55a;
    --green-main: #1b8a47;
    --green-dark: #156b37;
    --ink: #3a3a3a;
    --shadow: rgba(0, 0, 0, 0.22);
  }
  * { margin: 0; padding: 0; box-sizing: border-box; }
  html, body {
    width: 1200px;
    height: 1000px;
    overflow: hidden;
    background: var(--page-bg);
    font-family: "Roboto Condensed", Arial, sans-serif;
  }
  .canvas {
    position: relative;
    width: 1200px;
    height: 1000px;
  }
  .card {
    position: absolute;
    width: 600px;
    height: 343px;
    box-shadow: 0 6px 18px var(--shadow);
    overflow: hidden;
  }
  .card-front {
    left: 140px;
    top: 150px;
    background: var(--card-white);
  }
  .card-back {
    left: 500px;
    top: 520px;
    background: var(--green-main);
    display: flex;
    align-items: center;
    justify-content: center;
  }
  .front-waves {
    position: absolute;
    inset: 0;
    width: 100%;
    height: 100%;
  }
  .front-content {
    position: absolute;
    left: 48px;
    top: 108px;
  }
  .brand {
    display: flex;
    align-items: center;
    gap: 10px;
    margin-bottom: 22px;
  }
  .brand-mark {
    width: 14px;
    height: 14px;
    border-radius: 50%;
    background: var(--green-main);
  }
  .brand-name {
    font-size: 22px;
    font-weight: 400;
    color: var(--green-main);
    line-height: 1.15;
    max-width: 260px;
  }
  .person-name {
    font-size: 26px;
    font-weight: 700;
    color: var(--green-main);
    letter-spacing: 0.3px;
    line-height: 1;
    margin-left: 24px;
  }
  .person-title {
    font-size: 19px;
    color: var(--ink);
    margin: 4px 0 16px 24px;
  }
  .contact-list {
    list-style: none;
    margin-left: 24px;
    font-size: 16px;
    color: var(--ink);
    line-height: 1.2;
  }
  .back-brand {
    display: flex;
    align-items: center;
    gap: 16px;
  }
  .back-brand .brand-mark {
    width: 22px;
    height: 22px;
    background: var(--card-white);
  }
  .back-brand .brand-name {
    color: var(--card-white);
    font-size: 30px;
    max-width: 320px;
  }
</style>
</head>
<body>
<main class="canvas">
  <section class="card card-front" aria-label="Business card front">
    <svg class="front-waves" viewBox="0 0 600 343" preserveAspectRatio="none" aria-hidden="true">
      <rect x="0" y="0" width="600" height="343" fill="var(--green-dark)"/>
      <path d="M300 0 H560 C600 110 560 250 470 343 H300 Z" fill="var(--green-main)"/>
      <path d="M300 0 H470 C560 90 560 240 520 343 H300 Z" fill="var(--green-light)"/>
      <path d="M300 0 H430 C520 110 505 250 465 343 H300 Z" fill="var(--green-main)"/>
      <path d="M0 0 H310 C430 40 480 160 430 343 H0 Z" fill="var(--card-white)"/>
    </svg>
    <div class="front-content">
      <div class="brand">
        <span class="brand-mark"></span>
        <span class="brand-name">Halloway Crest Backers Guild</span>
      </div>
      <h1 class="person-name">DEAN VARROW</h1>
      <p class="person-title">Co-Founder / Investor</p>
      <ul class="contact-list">
        <li>555-314-2706</li>
        <li>deanvarrow@mailtern.net</li>
        <li>www.hcbackersguild.com</li>
      </ul>
    </div>
  </section>

  <section class="card card-back" aria-label="Business card back">
    <div class="back-brand">
      <span class="brand-mark"></span>
      <span class="brand-name">Halloway Crest Backers Guild</span>
    </div>
  </section>
</main>
</body>
</html>
```